Business Card Design

Just looking for a good designs that looks good with our company logo. I'd like it to be simple and to the point. Just including contact information, our logo, and my name somewhere on the card so future clients know who they're contacting, and a couple services offered. The two images I attached are pictures of our logo. I don't care which color they they are, I just attached both images to give a reference of logo colors depending on the color of the card.
Names: Calvin Prewitt
Phone: 555-247-9061
Email: tidyturfcrew@mailvista.net
Services offered:
Mowing
Fertilization
Aeration
Bed & tree maintenance
and more.
Industry/Entity Type
Business
Contact Information for Business Card
Names: Calvin Prewitt
Phone: 555-247-9061
Look and feel

```html
<!DOCTYPE html>
<html lang="en">
<head>
<meta charset="utf-8">
<title>Tidy Turf Crew – Business Card</title>
<link href="https://fonts.googleapis.com/css2?family=Roboto+Slab:wght@300;400&display=swap" rel="stylesheet">
<style>
  :root {
    --orange: #e9553d;
    --orange-light: #f59a86;
    --charcoal: #363a45;
    --slate: #8e9095;
    --paper-top: #ffffff;
    --paper-bottom: #e6e6e8;
    --ink: #1d1f24;
    --band-text: #f4f4f6;
  }
  html, body {
    margin: 0;
    padding: 0;
    overflow: hidden;
    background: #ffffff;
  }
  .card {
    position: relative;
    width: 1200px;
    height: 703px;
    overflow: hidden;
    background: linear-gradient(180deg, var(--paper-top) 0%, var(--paper-top) 35%, var(--paper-bottom) 80%);
    font-family: "Roboto Slab", Georgia, serif;
    font-weight: 300;
    color: var(--ink);
  }
  .corner-swoosh,
  .corner-texture {
    position: absolute;
    top: 0;
    left: 0;
    width: 1200px;
    height: 703px;
  }
  .brand {
    position: absolute;
    left: 60px;
    top: 128px;
    display: flex;
    align-items: center;
    gap: 24px;
  }
  .brand-dot {
    width: 104px;
    height: 104px;
    border-radius: 50%;
    background: var(--orange);
  }
  .brand-name {
    font-size: 58px;
    font-weight: 400;
    color: var(--charcoal);
    letter-spacing: 1px;
    line-height: 1;
  }
  .services {
    position: absolute;
    left: 605px;
    top: 258px;
  }
  .services-title {
    margin: 0 0 6px 28px;
    font-size: 35px;
    font-weight: 400;
    line-height: 1.2;
  }
  .services-list {
    list-style: none;
    margin: 0;
    padding: 0;
    font-size: 36px;
    font-weight: 400;
    line-height: 46px;
  }
  .services-list li {
    position: relative;
    padding-left: 22px;
  }
  .services-list li.bullet::before {
    content: "•";
    position: absolute;
    left: 0;
    color: var(--orange);
  }
  .owner-name {
    position: absolute;
    left: 70px;
    top: 496px;
    margin: 0;
    font-size: 44px;
    font-weight: 400;
  }
  .contact-band {
    position: absolute;
    left: 0;
    bottom: 0;
    width: 1200px;
    height: 140px;
    background: var(--charcoal);
    color: var(--band-text);
    display: flex;
    align-items: center;
    font-size: 40px;
    font-weight: 300;
  }
  .contact-item {
    display: flex;
    align-items: center;
  }
  .contact-phone { margin-left: 72px; }
  .contact-email { margin-left: 70px; }
  .contact-icon {
    fill: var(--band-text);
    margin-right: 22px;
  }
</style>
</head>
<body>
<div class="card">
  <svg class="corner-swoosh" viewBox="0 0 1200 703" aria-hidden="true">
    <path d="M865 0 C878 100 905 212 970 268 C1028 318 1110 340 1200 356 L1200 0 Z" fill="var(--slate)"/>
    <path d="M885 0 C897 95 922 200 985 254 C1040 300 1115 318 1200 330 L1200 0 Z" fill="var(--charcoal)"/>
    <path d="M903 0 C915 90 940 190 1000 240 C1050 285 1120 300 1200 312 L1200 0 Z" fill="var(--orange)"/>
  </svg>

  <svg class="corner-texture" viewBox="0 0 1200 703" role="img" aria-label="Soft halftone dot texture in the top right corner">
    <defs>
      <radialGradient id="corner-glow" cx="1200" cy="0" r="230" gradientUnits="userSpaceOnUse">
        <stop offset="0" stop-color="var(--orange-light)" stop-opacity="0.9"/>
        <stop offset="1" stop-color="var(--orange)" stop-opacity="0"/>
      </radialGradient>
    </defs>
    <ellipse cx="1200" cy="0" rx="225" ry="185" fill="url(#corner-glow)"/>
  </svg>

  <div class="brand">
    <div class="brand-dot"></div>
    <div class="brand-name">Tidy Turf Crew</div>
  </div>

  <section class="services">
    <h2 class="services-title">Services Offered</h2>
    <ul class="services-list">
      <li class="bullet">Mowing</li>
      <li class="bullet">Fertilization</li>
      <li class="bullet">Aeration</li>
      <li class="bullet">Bed &amp; tree maintenance</li>
      <li>and more.</li>
    </ul>
  </section>

  <h1 class="owner-name">Calvin Prewitt</h1>

  <footer class="contact-band">
    <div class="contact-item contact-phone">
      <svg class="contact-icon" width="24" height="40" viewBox="0 0 24 40" aria-hidden="true">
        <path d="M4 0h16a4 4 0 0 1 4 4v32a4 4 0 0 1-4 4H4a4 4 0 0 1-4-4V4a4 4 0 0 1 4-4zm0 6v26h16V6zm8 28a2 2 0 1 0 0 4 2 2 0 0 0 0-4z"/>
      </svg>
      <span>555-247-9061</span>
    </div>
    <div class="contact-item contact-email">
      <svg class="contact-icon" width="32" height="22" viewBox="0 0 32 22" aria-hidden="true">
        <path d="M0 0h32L16 12z"/>
        <path d="M0 3l10 8L0 20zM32 3v17l-10-9zM12 12.5l4 3 4-3L31 22H1z"/>
      </svg>
      <span>tidyturfcrew@mailvista.net</span>
    </div>
  </footer>
</div>
</body>
</html>
```